I need a SEO-friendly Wordpress website (making sure to style H1, H2, H3, etc correctly) for a Hawaii-based law firm called Meridian Crest Legal Group. Comparable websites include https://trvlaw.example/ and https://www.boultem.example/ for design reference. The current copy on the WelbyCounsel.example website can be used.

Coding

```html
<!DOCTYPE html>
<html lang="en">
<head>
<meta charset="utf-8">
<title>Meridian Crest Legal Group</title>
<link rel="stylesheet" href="https://fonts.googleapis.com/css2?family=Oswald:wght@400;500;600&family=Lato:wght@400;700&family=Tinos:wght@700&display=swap">
<style>
:root{
  --accent:#b5610f;
  --accent-dark:#8f4a08;
  --ink:#111111;
  --text:#555555;
  --dark:#121212;
  --dark-2:#1d1a17;
  --light:#efefef;
  --white:#ffffff;
}
*{box-sizing:border-box;margin:0;padding:0}
html,body{width:1200px;height:4373px;overflow:hidden}
body{position:relative;background:var(--white);font-family:'Lato',sans-serif;color:var(--text)}
.abs{position:absolute}
h1,h2,h3,.oswald{font-family:'Oswald',sans-serif;font-weight:500}

/* header */
.site-header{position:absolute;left:0;top:0;width:1200px;height:60px;background:#050505;z-index:5}
.brand{position:absolute;left:163px;top:14px;font-family:'Tinos',serif;font-weight:700;font-size:23px;color:var(--white)}
.main-nav{position:absolute;top:20px;left:0;width:1200px;font-family:'Oswald',sans-serif;font-size:12px;color:var(--white)}
.main-nav span{position:absolute;white-space:nowrap}
.phone-tab{position:absolute;left:857px;top:60px;width:180px;height:38px;background:var(--accent);clip-path:polygon(0 0,100% 0,92% 100%,8% 100%);color:var(--white);font-size:14px;text-align:center;line-height:38px;z-index:5}

/* hero */
.hero-bg{position:absolute;left:0;top:0;width:1200px;height:713px;
  background:radial-gradient(ellipse at 55% 40%,#3a3f4a 0%,#22252c 45%,#101216 100%);
  clip-path:polygon(0 0,100% 0,100% 501px,328px 713px,0 602px)}
.hero-title{position:absolute;left:0;top:190px;width:1200px;text-align:center;color:var(--white);font-size:60px;line-height:64px;font-weight:500}
.hero-sub{position:absolute;left:0;top:350px;width:1200px;text-align:center;color:var(--accent);font-size:16px}
.slide-arrow{position:absolute;width:37px;height:37px;background:var(--accent);display:flex;align-items:center;justify-content:center}

.vline{position:absolute;width:1px;background:var(--accent)}

/* welcome */
.welcome-photo{position:absolute;left:161px;top:808px;width:299px;height:411px;background:linear-gradient(180deg,#cfcbc4 0%,#5a5550 55%,#2b2826 100%)}
.welcome-title{position:absolute;left:500px;top:818px;width:539px;text-align:right;color:var(--ink);font-size:38px;line-height:46px}
.welcome-copy{position:absolute;left:510px;top:962px;width:529px;text-align:center;font-size:11.5px;line-height:19px;color:#666}
.welcome-copy p+p{margin-top:18px}
.btn{position:absolute;height:37px;background:var(--accent);color:var(--white);font-family:'Oswald',sans-serif;font-size:13px;display:flex;align-items:center;justify-content:center;overflow:hidden}
.btn::after{content:"";position:absolute;right:0;bottom:0;border-style:solid;border-width:0 0 9px 9px;border-color:transparent transparent var(--white) transparent}

/* practice */
.practice{position:absolute;left:0;top:1293px;width:1200px;height:612px;
  background:radial-gradient(ellipse at 20% 30%,#3a3530 0%,#1c1a18 50%,#0b0b0b 100%);
  clip-path:polygon(0 0,100% 0,100% 545px,600px 612px,0 545px)}
.practice-title{position:absolute;left:163px;top:1462px;color:var(--accent);font-size:38px;font-weight:500}
.practice-copy{position:absolute;left:163px;top:1543px;width:430px;color:#e6e6e6;font-size:11.5px;line-height:19.5px}
.practice-copy p+p{margin-top:19px}
.area-card{position:absolute;width:202px;height:202px;border:1px solid var(--accent);background:rgba(0,0,0,.35)}
.area-card h3{position:absolute;left:0;top:138px;width:100%;text-align:center;color:var(--white);font-size:17px}
.area-card svg.icon{position:absolute;left:71px;top:36px}
.plus{position:absolute;width:34px;height:34px;background:var(--accent);right:0;bottom:0}
.plus::before,.plus::after{content:"";position:absolute;background:var(--white);left:50%;top:50%}
.plus::before{width:18px;height:2px;transform:translate(-50%,-50%)}
.plus::after{width:2px;height:18px;transform:translate(-50%,-50%)}

/* attorneys */
.section-title{position:absolute;left:0;width:1200px;text-align:center;color:var(--ink);font-size:38px}
.attorney-name{position:absolute;left:0;top:2095px;width:1200px;text-align:center;color:var(--accent);font-size:18px}
.attorney-copy{position:absolute;left:310px;top:2138px;width:580px;text-align:center;font-size:11.5px;line-height:19px;color:#666}
.attorney-copy p+p{margin-top:19px}
.hline{position:absolute;left:0;top:2400px;width:1200px;height:1px;background:var(--accent)}

/* blog */
.post{position:absolute;top:2594px;width:278px;height:353px;background:var(--light)}
.post-thumb{height:187px}
.post h3{margin:14px 12px 0;font-size:15px;color:var(--ink);white-space:nowrap;overflow:hidden;text-overflow:ellipsis}
.post p{margin:6px 12px 0;font-size:11px;line-height:19px;color:#777}

/* social */
.connect{position:absolute;left:0;top:2985px;width:1200px;height:490px;
  background:radial-gradient(ellipse at 60% 60%,#3a2d22 0%,#231b15 50%,#120e0b 100%);
  clip-path:polygon(0 0,600px 55px,100% 0,100% 100%,0 100%)}
.diamond{position:absolute;width:78px;height:78px;border:1.5px solid var(--accent);transform:rotate(45deg)}
.diamond::after{content:"";position:absolute;left:50%;top:50%;width:18px;height:18px;border-radius:50%;background:var(--white);transform:translate(-50%,-50%)}
.connect-title{position:absolute;left:690px;top:3252px;width:240px;text-align:center;color:var(--accent);font-size:38px}

/* contact */
.contact-title{position:absolute;left:163px;top:3540px;color:var(--ink);font-size:38px}
.contact-line{position:absolute;display:flex;align-items:center;gap:12px;font-size:11.5px;color:#666}
.field{position:absolute;left:161px;width:428px;background:var(--light);font-size:11px;color:#777;padding:12px 16px}
.field.active{background:var(--white);border:1.5px solid var(--accent)}
.map{position:absolute;left:642px;top:3611px;width:558px;height:434px;background:linear-gradient(135deg,#e4e4e2 0%,#d6d7d3 100%)}
.directions{position:absolute;left:1039px;top:4001px;width:161px;height:44px;background:var(--accent);color:var(--white);font-family:'Oswald',sans-serif;font-size:17px;display:flex;align-items:center;justify-content:center;gap:12px}

/* footer */
.site-footer{position:absolute;left:0;top:4108px;width:1200px;height:265px;background:var(--dark)}
.footer-badge{position:absolute;left:577px;top:4178px;width:46px;height:46px;background:var(--accent);transform:rotate(45deg)}
.footer-brand{position:absolute;left:0;top:4236px;width:1200px;text-align:center;font-family:'Tinos',serif;font-weight:700;font-size:24px;color:var(--white)}
.footer-nav{position:absolute;left:0;top:4286px;width:1200px;text-align:center;font-family:'Oswald',sans-serif;font-size:11px;color:var(--accent)}
.footer-nav span{margin:0 14px}
.copyright{position:absolute;left:0;top:4342px;width:1200px;text-align:center;font-size:11px;color:#ddd}
</style>
</head>
<body>

<header class="site-header">
  <div class="brand">Meridian Crest Legal Group</div>
  <nav class="main-nav">
    <span style="left:690px">Home</span>
    <span style="left:746px">Practice Area</span>
    <span style="left:846px">Attorneys</span>
    <span style="left:930px">Blog</span>
    <span style="left:982px">Contact Us</span>
  </nav>
</header>
<div class="phone-tab">+1.808.555.0142</div>

<section>
  <div class="hero-bg" role="img" aria-label="Photo of attorneys in suits in a meeting, dark tone"></div>
  <h1 class="hero-title">Personal Injury Family &amp; Divorce<br>Child Custody</h1>
  <p class="hero-sub">Dedicated to making sure you receive the care and attention you need</p>
  <div class="slide-arrow" style="left:124px;top:307px"><svg width="12" height="18" viewBox="0 0 12 18"><path d="M9 2 3 9l6 7" fill="none" stroke="#fff" stroke-width="1.6"/></svg></div>
  <div class="slide-arrow" style="left:1039px;top:307px"><svg width="12" height="18" viewBox="0 0 12 18"><path d="M3 2l6 7-6 7" fill="none" stroke="#fff" stroke-width="1.6"/></svg></div>
</section>

<div class="vline" style="left:328px;top:713px;height:95px"></div>

<section>
  <div class="welcome-photo" role="img" aria-label="Photo of a judge in a robe holding an open book"></div>
  <h2 class="welcome-title">Welcome To Meridian Crest Legal Group</h2>
  <div class="welcome-copy">
    <p>The experienced attorneys in the Meridian Crest Legal Group's Kailua Kona, Hawaii office provide clients with a wide range of litigation expertise, including legal claims involving divorce &amp; family, personal injury, toxic exposures, intellectual property, and real estate.</p>
    <p>Our Kona office also offers commercial and hospitality litigation expertise on behalf of a wide variety of clients, including restaurants, hotels, property owners, and many others. We never wish to see our clients go to court, though if there is no other option, you're in safe hands with our seasoned trial lawyers and the many years of courtroom experience behind them.</p>
  </div>
  <div class="btn" style="left:949px;top:1158px;width:90px">Read More</div>
</section>

<section>
  <div class="practice" role="img" aria-label="Photo of lawyers shaking hands in a dark office"></div>
  <h2 class="practice-title">Our Practice Areas</h2>
  <div class="practice-copy">
    <p>The Big Island based attorneys of Meridian Crest Lawyers are licensed in several states, and specialize in numerous areas including divorce, family &amp; custody, personal injury, wrongful death, real estate, contract, and intellectual property.</p>
    <p>Click on the below areas of practice to learn more about our lawyers' experience and expertise in family law, personal injury, corporate, and real estate.</p>
  </div>
  <div class="btn" style="left:161px;top:1694px;width:90px">Our Services</div>

  <div class="area-card" style="left:611px;top:1375px">
    <svg class="icon" width="60" height="70" viewBox="0 0 60 70" fill="none" stroke="#fff" stroke-width="3"><path d="M30 6v50M12 14h36M12 14l-7 18h14zM48 14l-7 18h14zM20 60h20"/></svg>
    <h3>FAMILY &amp; DIVORCE</h3><span class="plus"></span>
  </div>
  <div class="area-card" style="left:837px;top:1375px">
    <svg class="icon" width="60" height="70" viewBox="0 0 60 70" fill="none" stroke="#fff" stroke-width="3"><circle cx="26" cy="8" r="5" fill="#fff"/><path d="M24 16v20h16l6 14"/><circle cx="24" cy="46" r="15"/></svg>
    <h3>PERSONAL INJURY</h3><span class="plus"></span>
  </div>
  <div class="area-card" style="left:611px;top:1601px">
    <svg class="icon" width="60" height="70" viewBox="0 0 60 70" fill="none" stroke="#fff" stroke-width="3"><rect x="4" y="18" width="52" height="38" rx="4"/><path d="M22 18v-7h16v7M4 34h52"/><rect x="25" y="30" width="10" height="8" fill="#fff"/></svg>
    <h3>CORPORATE &amp; IP</h3><span class="plus"></span>
  </div>
  <div class="area-card" style="left:837px;top:1601px">
    <svg class="icon" width="60" height="70" viewBox="0 0 60 70"><path d="M6 64V20h14V8h20v12h14v44z" fill="#fff"/><g fill="#1a1a1a"><rect x="12" y="28" width="6" height="8"/><rect x="42" y="28" width="6" height="8"/><rect x="27" y="16" width="6" height="8"/><rect x="12" y="44" width="6" height="8"/><rect x="42" y="44" width="6" height="8"/><rect x="25" y="48" width="10" height="16"/></g></svg>
    <h3>REAL ESTATE</h3><span class="plus"></span>
  </div>
</section>

<div class="vline" style="left:600px;top:1905px;height:100px"></div>

<section>
  <h2 class="section-title" style="top:1998px">Our Attorneys</h2>
  <h3 class="attorney-name">Daniel Okamura, ESQ.</h3>
  <div class="attorney-copy">
    <p>Daniel Okamura graduated from Westbrook University College of Law, in 1972. He graduated magna cum laude from Harlow University College of Law in 2008 receiving an LLM degree in international law.</p>
    <p>He has over 35 years of experience as both a personal injury lawyer, family law practictioner and real estate counsel serving as general counsel for multi-national corporations, and is a licensed real estate broker in both Hawaii and California. Okamura has been based in Kailua Kona for more than 20 years.</p>
  </div>
  <div class="slide-arrow" style="left:124px;top:2198px"><svg width="12" height="18" viewBox="0 0 12 18"><path d="M9 2 3 9l6 7" fill="none" stroke="#fff" stroke-width="1.6"/></svg></div>
  <div class="slide-arrow" style="left:1039px;top:2198px"><svg width="12" height="18" viewBox="0 0 12 18"><path d="M3 2l6 7-6 7" fill="none" stroke="#fff" stroke-width="1.6"/></svg></div>
  <div class="btn" style="left:555px;top:2295px;width:90px">Read More</div>
</section>

<div class="hline"></div>
<div class="vline" style="left:600px;top:2400px;height:88px"></div>

<section>
  <h2 class="section-title" style="top:2496px">Latest Blog</h2>
  <article class="post" style="left:161px">
    <div class="post-thumb" role="img" aria-label="Photo of parents kissing their baby" style="background:linear-gradient(135deg,#b98a9a,#7d5a66)"></div>
    <h3>Top 10 Things to Do Before Filing...</h3>
    <p>No one gets married with the intention of things not working out, but it's an unfortunate fact that many marriages don't work out in the end.</p>
    <span class="plus" style="right:0;bottom:16px;width:37px;height:37px"></span>
  </article>
  <article class="post" style="left:462px">
    <div class="post-thumb" role="img" aria-label="Photo of a judge writing at a desk with law books" style="background:linear-gradient(135deg,#5a4636,#221a14)"></div>
    <h3>Top 15 Things to Do During Custody...</h3>
    <p>It's already tragic enough when two people who planned on spending their lives together no longer wish to see that dream through, but to compound</p>
    <span class="plus" style="right:0;bottom:16px;width:37px;height:37px"></span>
  </article>
  <article class="post" style="left:760px">
    <div class="post-thumb" role="img" aria-label="Photo of three businessmen talking at a table" style="background:linear-gradient(135deg,#d9dde2,#7d838c)"></div>
    <h3>Lorem Ipsum is simply dummy text ...</h3>
    <p>Lorem Ipsum is simply dummy text of the printing and typesetting industry. Lorem Ipsum has been the industry's standard dummy text ever since the</p>
    <span class="plus" style="right:0;bottom:16px;width:37px;height:37px"></span>
  </article>
</section>

<section>
  <div class="connect" role="img" aria-label="Photo of a gavel and scales of justice, dark tone"></div>
  <div class="diamond" style="left:256px;top:3161px"></div>
  <div class="diamond" style="left:390px;top:3161px"></div>
  <div class="diamond" style="left:323px;top:3229px"></div>
  <div class="diamond" style="left:458px;top:3229px"></div>
  <div class="diamond" style="left:256px;top:3297px"></div>
  <div class="diamond" style="left:390px;top:3297px"></div>
  <div class="vline" style="left:810px;top:3149px;height:93px"></div>
  <h2 class="connect-title">Stay Connected</h2>
</section>

<section>
  <h2 class="contact-title">Contact Us</h2>
  <div class="contact-line" style="left:161px;top:3643px">
    <svg width="18" height="18" viewBox="0 0 18 18"><path d="M4 1l3 4-2 2c1 3 3 5 6 6l2-2 4 3-2 3C8 17 1 10 1 3z" fill="var(--accent)"/></svg>+1.808.555.0142
  </div>
  <div class="contact-line" style="left:326px;top:3643px">
    <svg width="20" height="14" viewBox="0 0 20 14"><rect width="20" height="14" fill="var(--accent)"/><path d="M1 1l9 7 9-7" fill="none" stroke="#fff" stroke-width="1.5"/></svg>clients@welbycounsel.example
  </div>
  <div class="contact-line" style="left:161px;top:3692px">
    <svg width="16" height="20" viewBox="0 0 16 20"><path d="M8 0a8 8 0 0 1 8 8c0 5-8 12-8 12S0 13 0 8a8 8 0 0 1 8-8z" fill="var(--accent)"/><circle cx="8" cy="8" r="3" fill="#fff"/></svg>410 Harbor View Road, Suite 212, Kailua Kona, Hawaii 96740.
  </div>
  <div class="field active" style="top:3748px;height:45px">Name:</div>
  <div class="field" style="top:3808px;height:44px">Phone:</div>
  <div class="field" style="top:3867px;height:88px">Message:</div>
  <div class="btn" style="left:161px;top:4006px;width:90px">Submit Now</div>
  <div class="map" role="img" aria-label="Street map of Kailua Kona showing the office location"></div>
  <div class="directions">Get Directions
    <svg width="22" height="14" viewBox="0 0 22 14"><path d="M0 7h20M14 1l6 6-6 6" fill="none" stroke="#fff" stroke-width="1.8"/></svg>
  </div>
</section>

<footer class="site-footer"></footer>
<div class="footer-badge"></div>
<svg class="abs" style="left:588px;top:4192px" width="24" height="14" viewBox="0 0 24 14"><path d="M2 12l10-9 10 9" fill="none" stroke="#fff" stroke-width="2"/></svg>
<div class="footer-brand">Meridian Crest Legal Group</div>
<nav class="footer-nav"><span>Home</span><span>Practice Area</span><span>Attorneys</span><span>Blog</span><span>Contact Us</span></nav>
<p class="copyright">Copyrights 2019 © Meridian Crest Legal Group. All Rights Reserved. Terms &amp; Conditions | Privacy Policy</p>

</body>
</html>
```